Marlow Airwaves needs a functional Internet Radio App

We need a Internet Radio app design for IOS and Android,
Beamcore/ Frostline Stream( BEAMCORE playlist (.pls) file or Frostline (.m3u) playlist file) Supported streams: AAC, AAC+, HE-AAC+.
Should supports Tunevault, Mixbench Pro, Zimbo, Spinlane
Here are some of the features we need you to include in the design:
1. Multi Stream player with Scheduling
2. Track Display
3. Track Sharing ( Friendloop and other)
4. Album Cover display( automatic cover retrieval base on track)
5.Track Purchases ( Songbarn and Parcelo )
6.Push Notification( Geo-localize outgoing data and schedule messages)
7. News, Podcasts and Videos ( Live Feed)
8. Alarms
9. Incorporate "Dedications" ( Listeners love to see when their message is published in real time)
10.Ad management ( management system for the app)
11.Listeners should be able to 'Skip song'
12. Database for music

Target Market(s)

Everyone

Industry/Entity Type

Radio Station

Font styles to use
Decorative

Colors
3176b5
0355a3
85acd3
ffffff

Requirements
Must have
• 1.I need a functional app
• 2. Song Request
Nice to have
• N/A
Should not have
• Other Radio Station app design

```html
<!DOCTYPE html>
<html lang="en">
<head>
<meta charset="utf-8">
<title>Marlow Airwaves – App Screens</title>
<link rel="stylesheet" href="https://fonts.googleapis.com/css2?family=Roboto:wght@400;500;700&display=swap">
<style>
  :root {
    --brand-blue: #3176b5;
    --brand-deep: #0355a3;
    --brand-soft: #85acd3;
    --white: #ffffff;
    --page-bg: #c9eaf1;
    --aqua: #4fb6d8;
    --aqua-dark: #2f8fcd;
    --screen-top: #eef9fc;
    --screen-bottom: #8fd2e4;
    --ink: #3b4a55;
    --ink-soft: #7d8d98;
    --rule: #cfe6ee;
    --menu-panel: #6d7476;
    --menu-rule: #8a9193;
    --ad-bg: #111417;
    --alert: #e8433a;
    --star: #f2c230;
  }
  * { box-sizing: border-box; margin: 0; padding: 0; }
  html, body { width: 1200px; height: 539px; overflow: hidden; }
  body {
    background: var(--page-bg);
    font-family: "Roboto", Arial, sans-serif;
    color: var(--ink);
    position: relative;
  }

  .screen {
    position: absolute;
    top: 142px;
    width: 126px;
    height: 224px;
    overflow: hidden;
    background: linear-gradient(180deg, var(--screen-top) 0%, #cdeef6 45%, var(--screen-bottom) 100%);
    box-shadow: 0 2px 6px rgba(0, 60, 90, 0.18);
  }
  .screen--home { left: 126px; }
  .screen--touch { left: 331px; }
  .screen--notifications { left: 535px; background: var(--white); }
  .screen--menu { left: 739px; }
  .screen--search { left: 940px; background: var(--white); }

  /* top bar */
  .top-bar {
    position: absolute; top: 0; left: 0; right: 0; height: 30px;
    display: flex; align-items: center; justify-content: space-between; padding: 0 12px;
  }
  .hamburger { width: 12px; height: 9px; display: flex; flex-direction: column; justify-content: space-between; }
  .hamburger span { display: block; height: 1.6px; background: var(--brand-blue); border-radius: 1px; }
  .search-auto { display: flex; align-items: center; gap: 2px; }
  .auto-pill {
    font-size: 3.5px; font-weight: 700; color: var(--white); background: var(--brand-blue);
    border-radius: 3px; padding: 1px 3px; letter-spacing: .2px;
  }

  /* brand */
  .brand-mark {
    position: absolute; left: 0; right: 0; top: 88px;
    text-align: center; font-size: 9px; font-weight: 700; color: var(--brand-blue);
  }
  .touch-ring {
    position: absolute; left: 33px; top: 60px; width: 60px; height: 60px; border-radius: 50%;
    background: radial-gradient(circle, #f7fdff 0 55%, #d3eef7 56% 64%, #9fd9ea 65% 100%);
    border: 2px solid #7cc8e2;
    display: flex; align-items: center; justify-content: center;
    font-size: 5.5px; font-weight: 700; color: var(--brand-blue); text-align: center; line-height: 1.2;
  }
  .touch-label {
    position: absolute; left: 0; right: 0; top: 130px; text-align: center;
    font-size: 9px; color: var(--white); letter-spacing: .3px;
  }

  /* ad banner */
  .ad-banner {
    position: absolute; left: 0; right: 0; top: 168px; height: 18px;
    background: var(--ad-bg); display: flex; align-items: center; padding: 0 3px; gap: 3px;
  }
  .ad-art {
    width: 12px; height: 12px; border-radius: 2px;
    background: linear-gradient(135deg, #e83a7a, #f6c43a 50%, #3aa8e8);
  }
  .ad-copy { flex: 1; color: var(--white); line-height: 1.1; }
  .ad-title { font-size: 5px; font-weight: 700; }
  .ad-meta { font-size: 3.8px; display: flex; gap: 3px; align-items: center; }
  .ad-free { background: var(--white); color: var(--ad-bg); padding: 0 1.5px; font-weight: 700; }
  .ad-stars { color: var(--star); }
  .ad-get {
    width: 11px; height: 11px; background: #2c6fe0; border-radius: 1px;
    display: flex; align-items: center; justify-content: center;
  }

  /* tab bar */
  .tab-bar {
    position: absolute; left: 0; right: 0; bottom: 0; height: 38px;
    background: linear-gradient(180deg, var(--aqua) 0%, var(--aqua-dark) 100%);
    display: flex; justify-content: space-around; align-items: center; padding: 0 2px;
  }
  .tab { display: flex; flex-direction: column; align-items: center; gap: 2px; width: 24px; position: relative; padding: 4px 0; }
  .tab span { font-size: 3.5px; color: var(--white); }
  .tab svg { width: 11px; height: 11px; }
  .tab--active { background: rgba(255, 255, 255, 0.18); }
  .badge { position: absolute; top: 2px; right: 5px; width: 3.5px; height: 3.5px; border-radius: 50%; background: var(--alert); }

  /* notifications */
  .segmented {
    position: absolute; top: 5px; left: 10px; right: 10px; height: 13px;
    display: flex; border: 1px solid var(--aqua); border-radius: 3px; overflow: hidden;
  }
  .segmented div { flex: 1; font-size: 6px; display: flex; align-items: center; justify-content: center; color: var(--aqua); }
  .segmented .is-active { background: var(--aqua); color: var(--white); }
  .notice-list { position: absolute; top: 24px; left: 0; right: 0; }
  .day-head {
    height: 7px; background: #c3e6f1; font-size: 4px; color: var(--white);
    display: flex; align-items: center; justify-content: space-between; padding: 0 6px 0 24px;
  }
  .day-head i { width: 4px; height: 4px; border-radius: 50%; background: var(--aqua); display: block; }
  .track-row {
    height: 20px; display: flex; align-items: center; gap: 3px; padding: 0 8px;
    border-bottom: 1px solid var(--rule);
  }
  .cover { width: 16px; height: 16px; background: linear-gradient(135deg, #d6e4ea, #7f98a6); flex: none; }
  .track-text { line-height: 1.15; flex: 1; }
  .track-artist { font-size: 4.5px; color: var(--ink); }
  .track-title { font-size: 4.5px; color: var(--ink-soft); }
  .track-time { font-size: 3px; color: var(--aqua); }
  .pull-handle { position: absolute; bottom: 4px; left: 56px; width: 14px; height: 4px; }

  /* menu */
  .menu-panel {
    position: absolute; left: 0; top: 0; width: 112px; height: 168px;
    background: linear-gradient(180deg, #8a9294, var(--menu-panel));
  }
  .menu-strip { position: absolute; right: 0; top: 0; width: 14px; height: 168px; background: rgba(255,255,255,.35); }
  .menu-strip .hamburger { position: absolute; top: 10px; left: 1px; width: 11px; }
  .menu-strip .hamburger span { background: #4d5557; }
  .menu-search {
    position: absolute; top: 6px; left: 3px; width: 92px; height: 12px; border-radius: 6px; background: var(--white);
    display: flex; align-items: center; padding-left: 3px;
  }
  .menu-gear { position: absolute; top: 9px; left: 99px; width: 6px; height: 6px; border-radius: 50%; border: 1.3px solid #b9c0c2; }
  .menu-list { position: absolute; top: 24px; left: 0; width: 112px; list-style: none; }
  .menu-list li {
    height: 15.5px; font-size: 5px; color: var(--white); display: flex; align-items: center;
    padding-left: 6px; border-bottom: 1px solid var(--menu-rule);
  }

  /* search screen */
  .search-head { position: absolute; top: 0; left: 0; right: 0; height: 28px; display: flex; align-items: center; padding: 0 10px; }
  .back-pill { font-size: 3.5px; color: var(--white); background: var(--aqua); border-radius: 2px; padding: 1px 3px; }
  .search-title { flex: 1; text-align: center; font-size: 5.5px; color: var(--aqua); }
  .search-field {
    position: absolute; top: 29px; left: 10px; right: 10px; height: 14px; border-radius: 7px;
    border: 1px solid #cfe2ea; background: #f4fafc; display: flex; align-items: center; gap: 4px; padding-left: 4px;
  }
  .search-field span { font-size: 5px; color: #b7c6cd; flex: 1; text-align: center; padding-right: 14px; }
  .filter-tabs {
    position: absolute; top: 46px; left: 0; right: 0; height: 14px; display: flex;
    border-bottom: 1.5px solid var(--aqua);
  }
  .filter-tabs div { flex: 1; font-size: 5.5px; color: var(--aqua); display: flex; align-items: center; justify-content: center; border-right: 1px solid var(--rule); }
  .filter-tabs div:last-child { border-right: none; }
  .filter-tabs .is-active { background: var(--aqua); color: var(--white); }
  .artist-list { position: absolute; top: 63px; left: 0; right: 0; }
  .artist-list .track-row { height: 21px; padding: 0 6px; }
  .row-actions { display: flex; gap: 3px; align-items: center; }
  .row-actions svg { width: 6px; height: 6px; }
</style>
</head>
<body>

<!-- Splash screen -->
<section class="screen screen--home">
  <header class="top-bar">
    <div class="hamburger"><span></span><span></span><span></span></div>
    <div class="search-auto">
      <svg width="9" height="9" viewBox="0 0 24 24" fill="none" stroke="var(--brand-blue)" stroke-width="3"><circle cx="10" cy="10" r="6"/><path d="M15 15l6 6"/></svg>
      <span class="auto-pill">AUTO</span>
    </div>
  </header>
  <div class="brand-mark">Marlow Airwaves</div>
  <aside class="ad-banner">
    <div class="ad-art" role="img" aria-label="Advertised game icon"></div>
    <div class="ad-copy">
      <div class="ad-title">Puddle Pop</div>
      <div class="ad-meta"><span class="ad-free">FREE</span><span class="ad-stars">★★★★★</span><span>13678 Reviews</span></div>
    </div>
    <div class="ad-get"><svg width="7" height="7" viewBox="0 0 24 24" fill="var(--white)"><path d="M9 3h6v9h5l-8 9-8-9h5z"/></svg></div>
  </aside>
  <nav class="tab-bar">
    <div class="tab"><svg viewBox="0 0 24 24" fill="none" stroke="#fff" stroke-width="2"><circle cx="12" cy="12" r="2" fill="#fff"/><path d="M8 8a5.6 5.6 0 000 8M16 8a5.6 5.6 0 010 8M5 5a10 10 0 000 14M19 5a10 10 0 010 14"/></svg><span>Stations</span></div>
    <div class="tab"><svg viewBox="0 0 24 24" fill="none" stroke="#fff" stroke-width="2.6"><circle cx="10" cy="10" r="6"/><path d="M15 15l6 6"/></svg><span>Search</span></div>
    <div class="tab"><svg viewBox="0 0 24 24"><rect x="2" y="5" width="20" height="14" fill="#fff"/><path d="M2 5l10 8 10-8" fill="none" stroke="var(--aqua-dark)" stroke-width="1.5"/></svg><i class="badge"></i><span>Message</span></div>
    <div class="tab"><svg viewBox="0 0 24 24" fill="none" stroke="#fff" stroke-width="2"><circle cx="12" cy="13" r="7"/><path d="M12 9v4l3 2M4 6l3-3M20 6l-3-3"/></svg><span>Alarm</span></div>
    <div class="tab"><svg viewBox="0 0 24 24" fill="#fff"><circle cx="5" cy="12" r="2.2"/><circle cx="12" cy="12" r="2.2"/><circle cx="19" cy="12" r="2.2"/></svg><span>More</span></div>
  </nav>
</section>

<!-- Touch to play -->
<section class="screen screen--touch">
  <header class="top-bar">
    <div class="hamburger"><span></span><span></span><span></span></div>
    <div class="search-auto">
      <svg width="9" height="9" viewBox="0 0 24 24" fill="none" stroke="var(--brand-blue)" stroke-width="3"><circle cx="10" cy="10" r="6"/><path d="M15 15l6 6"/></svg>
      <span class="auto-pill">AUTO</span>
    </div>
  </header>
  <div class="touch-ring">Marlow<br>Airwaves</div>
  <div class="touch-label">Touch</div>
  <aside class="ad-banner">
    <div class="ad-art" role="img" aria-label="Advertised game icon"></div>
    <div class="ad-copy">
      <div class="ad-title">Puddle Pop</div>
      <div class="ad-meta"><span class="ad-free">FREE</span><span class="ad-stars">★★★★★</span><span>13678 Reviews</span></div>
    </div>
    <div class="ad-get"><svg width="7" height="7" viewBox="0 0 24 24" fill="var(--white)"><path d="M9 3h6v9h5l-8 9-8-9h5z"/></svg></div>
  </aside>
  <nav class="tab-bar">
    <div class="tab"><svg viewBox="0 0 24 24" fill="none" stroke="#fff" stroke-width="2"><circle cx="12" cy="12" r="2" fill="#fff"/><path d="M8 8a5.6 5.6 0 000 8M16 8a5.6 5.6 0 010 8M5 5a10 10 0 000 14M19 5a10 10 0 010 14"/></svg><span>Stations</span></div>
    <div class="tab"><svg viewBox="0 0 24 24" fill="none" stroke="#fff" stroke-width="2.6"><circle cx="10" cy="10" r="6"/><path d="M15 15l6 6"/></svg><span>Search</span></div>
    <div class="tab"><svg viewBox="0 0 24 24"><rect x="2" y="5" width="20" height="14" fill="#fff"/><path d="M2 5l10 8 10-8" fill="none" stroke="var(--aqua-dark)" stroke-width="1.5"/></svg><i class="badge"></i><span>Message</span></div>
    <div class="tab"><svg viewBox="0 0 24 24" fill="none" stroke="#fff" stroke-width="2"><circle cx="12" cy="13" r="7"/><path d="M12 9v4l3 2M4 6l3-3M20 6l-3-3"/></svg><span>Alarm</span></div>
    <div class="tab"><svg viewBox="0 0 24 24" fill="#fff"><circle cx="5" cy="12" r="2.2"/><circle cx="12" cy="12" r="2.2"/><circle cx="19" cy="12" r="2.2"/></svg><span>More</span></div>
  </nav>
</section>

<!-- Notifications -->
<section class="screen screen--notifications">
  <div class="segmented"><div>Today</div><div class="is-active">Notifications</div></div>
  <div class="notice-list">
    <div class="day-head">Today<i></i></div>
    <div class="track-row"><div class="cover" role="img" aria-label="Album cover"></div><div class="track-text"><div class="track-artist">LENA MARSH</div><div class="track-title">Velvet</div><div class="track-time">10:24 AM</div></div></div>
    <div class="track-row"><div class="cover" role="img" aria-label="Album cover"></div><div class="track-text"><div class="track-artist">LENA MARSH</div><div class="track-title">Velvet</div><div class="track-time">09:12 AM</div></div></div>
    <div class="day-head">Yesterday<i></i></div>
    <div class="track-row"><div class="cover" role="img" aria-label="Album cover"></div><div class="track-text"><div class="track-artist">LENA MARSH</div><div class="track-title">Velvet</div><div class="track-time">08:40 PM</div></div></div>
    <div class="track-row"><div class="cover" role="img" aria-label="Album cover"></div><div class="track-text"><div class="track-artist">LENA MARSH</div><div class="track-title">Velvet</div><div class="track-time">06:15 PM</div></div></div>
    <div class="track-row"><div class="cover" role="img" aria-label="Album cover"></div><div class="track-text"><div class="track-artist">LENA MARSH</div><div class="track-title">Velvet</div><div class="track-time">02:30 PM</div></div></div>
    <div class="track-row"><div class="cover" role="img" aria-label="Album cover"></div><div class="track-text"><div class="track-artist">LENA MARSH</div><div class="track-title">Velvet</div><div class="track-time">11:05 AM</div></div></div>
    <div class="day-head">Tuesday<i></i></div>
    <div class="track-row"><div class="cover" role="img" aria-label="Album cover"></div><div class="track-text"><div class="track-artist">LENA MARSH</div><div class="track-title">Velvet</div><div class="track-time">07:50 PM</div></div></div>
  </div>
  <svg class="pull-handle" viewBox="0 0 14 4"><path d="M1 3.5Q7 -1 13 3.5" fill="none" stroke="var(--aqua)" stroke-width="1.6" stroke-linecap="round"/></svg>
</section>

<!-- Side menu -->
<section class="screen screen--menu">
  <div class="menu-panel">
    <div class="menu-search"><svg width="8" height="8" viewBox="0 0 24 24" fill="none" stroke="var(--aqua)" stroke-width="3"><circle cx="10" cy="10" r="6"/><path d="M15 15l6 6"/></svg></div>
    <div class="menu-gear"></div>
    <ul class="menu-list">
      <li>Live Feed</li>
      <li>Song Request</li>
      <li>Live &amp; Spinlane</li>
      <li>Radio Stations</li>
      <li>xxxxxxxxxxx</li>
      <li>xxxxxxxxx</li>
      <li>xxxxxxxxx</li>
      <li>xxxxxxx</li>
    </ul>
  </div>
  <div class="menu-strip"><div class="hamburger"><span></span><span></span><span></span></div></div>
  <aside class="ad-banner">
    <div class="ad-art" role="img" aria-label="Advertised game icon"></div>
    <div class="ad-copy">
      <div class="ad-title">Puddle Pop</div>
      <div class="ad-meta"><span class="ad-free">FREE</span><span class="ad-stars">★★★★★</span><span>13678 Reviews</span></div>
    </div>
    <div class="ad-get"><svg width="7" height="7" viewBox="0 0 24 24" fill="var(--white)"><path d="M9 3h6v9h5l-8 9-8-9h5z"/></svg></div>
  </aside>
  <nav class="tab-bar">
    <div class="tab"><svg viewBox="0 0 24 24" fill="none" stroke="#fff" stroke-width="2"><circle cx="12" cy="12" r="2" fill="#fff"/><path d="M8 8a5.6 5.6 0 000 8M16 8a5.6 5.6 0 010 8M5 5a10 10 0 000 14M19 5a10 10 0 010 14"/></svg><span>Stations</span></div>
    <div class="tab"><svg viewBox="0 0 24 24" fill="none" stroke="#fff" stroke-width="2.6"><circle cx="10" cy="10" r="6"/><path d="M15 15l6 6"/></svg><span>Search</span></div>
    <div class="tab"><svg viewBox="0 0 24 24"><rect x="2" y="5" width="20" height="14" fill="#fff"/><path d="M2 5l10 8 10-8" fill="none" stroke="var(--aqua-dark)" stroke-width="1.5"/></svg><i class="badge"></i><span>Message</span></div>
    <div class="tab"><svg viewBox="0 0 24 24" fill="none" stroke="#fff" stroke-width="2"><circle cx="12" cy="13" r="7"/><path d="M12 9v4l3 2M4 6l3-3M20 6l-3-3"/></svg><span>Alarm</span></div>
    <div class="tab"><svg viewBox="0 0 24 24" fill="#fff"><circle cx="5" cy="12" r="2.2"/><circle cx="12" cy="12" r="2.2"/><circle cx="19" cy="12" r="2.2"/></svg><span>More</span></div>
  </nav>
</section>

<!-- Search results -->
<section class="screen screen--search">
  <header class="search-head">
    <span class="back-pill">Back</span>
    <span class="search-title">Search</span>
    <div class="hamburger"><span></span><span></span><span></span></div>
  </header>
  <div class="search-field">
    <svg width="7" height="7" viewBox="0 0 24 24" fill="none" stroke="#b7c6cd" stroke-width="3"><circle cx="10" cy="10" r="6"/><path d="M15 15l6 6"/></svg>
    <span>LENA MARSH</span>
  </div>
  <div class="filter-tabs"><div>Playlists</div><div>HITS</div><div class="is-active">Artists</div><div>Album</div></div>
  <div class="artist-list">
    <div class="track-row"><div class="cover" role="img" aria-label="Artist photo"></div><div class="track-text"><div class="track-artist">LENA MARSH</div><div class="track-title">Velvet</div></div>
      <div class="row-actions">
        <svg viewBox="0 0 24 24" fill="none" stroke="var(--ink-soft)" stroke-width="2.5"><circle cx="5" cy="12" r="3"/><circle cx="19" cy="5" r="3"/><circle cx="19" cy="19" r="3"/><path d="M8 11l8-5M8 13l8 5"/></svg>
        <svg viewBox="0 0 24 24" fill="none" stroke="var(--aqua)" stroke-width="2.5"><circle cx="12" cy="12" r="10"/><path d="M10 8l6 4-6 4z" fill="var(--aqua)"/></svg>
        <svg viewBox="0 0 24 24" fill="none" stroke="var(--aqua)" stroke-width="2.5"><path d="M2 4h4l3 11h11l2-8H7"/><circle cx="10" cy="20" r="1.5"/><circle cx="18" cy="20" r="1.5"/></svg>
      </div></div>
    <div class="track-row"><div class="cover" role="img" aria-label="Artist photo"></div><div class="track-text"><div class="track-artist">LENA MARSH</div><div class="track-title">Velvet</div></div>
      <div class="row-actions">
        <svg viewBox="0 0 24 24" fill="none" stroke="var(--ink-soft)" stroke-width="2.5"><circle cx="5" cy="12" r="3"/><circle cx="19" cy="5" r="3"/><circle cx="19" cy="19" r="3"/><path d="M8 11l8-5M8 13l8 5"/></svg>
        <svg viewBox="0 0 24 24" fill="none" stroke="var(--aqua)" stroke-width="2.5"><circle cx="12" cy="12" r="10"/><path d="M10 8l6 4-6 4z" fill="var(--aqua)"/></svg>
        <svg viewBox="0 0 24 24" fill="none" stroke="var(--aqua)" stroke-width="2.5"><path d="M2 4h4l3 11h11l2-8H7"/><circle cx="10" cy="20" r="1.5"/><circle cx="18" cy="20" r="1.5"/></svg>
      </div></div>
    <div class="track-row"><div class="cover" role="img" aria-label="Artist photo"></div><div class="track-text"><div class="track-artist">LENA MARSH</div><div class="track-title">Velvet</div></div>
      <div class="row-actions">
        <svg viewBox="0 0 24 24" fill="none" stroke="var(--ink-soft)" stroke-width="2.5"><circle cx="5" cy="12" r="3"/><circle cx="19" cy="5" r="3"/><circle cx="19" cy="19" r="3"/><path d="M8 11l8-5M8 13l8 5"/></svg>
        <svg viewBox="0 0 24 24" fill="none" stroke="var(--aqua)" stroke-width="2.5"><circle cx="12" cy="12" r="10"/><path d="M10 8l6 4-6 4z" fill="var(--aqua)"/></svg>
        <svg viewBox="0 0 24 24" fill="none" stroke="var(--aqua)" stroke-width="2.5"><path d="M2 4h4l3 11h11l2-8H7"/><circle cx="10" cy="20" r="1.5"/><circle cx="18" cy="20" r="1.5"/></svg>
      </div></div>
    <div class="track-row"><div class="cover" role="img" aria-label="Artist photo"></div><div class="track-text"><div class="track-artist">LENA MARSH</div><div class="track-title">Velvet</div></div>
      <div class="row-actions">
        <svg viewBox="0 0 24 24" fill="none" stroke="var(--ink-soft)" stroke-width="2.5"><circle cx="5" cy="12" r="3"/><circle cx="19" cy="5" r="3"/><circle cx="19" cy="19" r="3"/><path d="M8 11l8-5M8 13l8 5"/></svg>
        <svg viewBox="0 0 24 24" fill="none" stroke="var(--aqua)" stroke-width="2.5"><circle cx="12" cy="12" r="10"/><path d="M10 8l6 4-6 4z" fill="var(--aqua)"/></svg>
        <svg viewBox="0 0 24 24" fill="none" stroke="var(--aqua)" stroke-width="2.5"><path d="M2 4h4l3 11h11l2-8H7"/><circle cx="10" cy="20" r="1.5"/><circle cx="18" cy="20" r="1.5"/></svg>
      </div></div>
    <div class="track-row"><div class="cover" role="img" aria-label="Artist photo"></div><div class="track-text"><div class="track-artist">LENA MARSH</div><div class="track-title">Velvet</div></div>
      <div class="row-actions">
        <svg viewBox="0 0 24 24" fill="none" stroke="var(--ink-soft)" stroke-width="2.5"><circle cx="5" cy="12" r="3"/><circle cx="19" cy="5" r="3"/><circle cx="19" cy="19" r="3"/><path d="M8 11l8-5M8 13l8 5"/></svg>
        <svg viewBox="0 0 24 24" fill="none" stroke="var(--aqua)" stroke-width="2.5"><circle cx="12" cy="12" r="10"/><path d="M10 8l6 4-6 4z" fill="var(--aqua)"/></svg>
        <svg viewBox="0 0 24 24" fill="none" stroke="var(--aqua)" stroke-width="2.5"><path d="M2 4h4l3 11h11l2-8H7"/><circle cx="10" cy="20" r="1.5"/><circle cx="18" cy="20" r="1.5"/></svg>
      </div></div>
  </div>
  <nav class="tab-bar">
    <div class="tab"><svg viewBox="0 0 24 24" fill="none" stroke="#fff" stroke-width="2"><circle cx="12" cy="12" r="2" fill="#fff"/><path d="M8 8a5.6 5.6 0 000 8M16 8a5.6 5.6 0 010 8M5 5a10 10 0 000 14M19 5a10 10 0 010 14"/></svg><span>Stations</span></div>
    <div class="tab tab--active"><svg viewBox="0 0 24 24" fill="none" stroke="#fff" stroke-width="2.6"><circle cx="10" cy="10" r="6"/><path d="M15 15l6 6"/></svg><span>Search</span></div>
    <div class="tab"><svg viewBox="0 0 24 24"><rect x="2" y="5" width="20" height="14" fill="#fff"/><path d="M2 5l10 8 10-8" fill="none" stroke="var(--aqua-dark)" stroke-width="1.5"/></svg><span>Message</span></div>
    <div class="tab"><svg viewBox="0 0 24 24" fill="none" stroke="#fff" stroke-width="2"><circle cx="12" cy="13" r="7"/><path d="M12 9v4l3 2M4 6l3-3M20 6l-3-3"/></svg><span>Alarm</span></div>
    <div class="tab"><svg viewBox="0 0 24 24" fill="#fff"><circle cx="5" cy="12" r="2.2"/><circle cx="12" cy="12" r="2.2"/><circle cx="19" cy="12" r="2.2"/></svg><span>More</span></div>
  </nav>
</section>

</body>
</html>
```